Mortgage Loan officer needs clean/modern business card design

Looking for a clean, modern 2-sided business card design. We like the earth tones used in our logo and website http://varnhill-lending.com . Would also like to incorporate: 1) Something special to make our card stand out - a pop of color or embossed logo, for instance and 2) please include "Mortgage Loans" "Reverse Mortgages" "Private Money Loans" on back of card with the logo.

Front: Needs to include agent/company license info - see website. Agent name: Marco Lindqvist

Here are fonts and colors used for our logo:
Font: Avenir Next
Colors:
#2c3539 - Dark Gray
#576870 - Light Gray
#ffffff - Background White

Target Market(s)

Prospects and current clients. Will also be distributing to people in professional network (attorneys and CPAs)

Industry/Entity Type

Business

Contact Information for Business Card

Include agent name, contact info, website on front, licensing info for agent an company. Logo and services offered on back

Font styles to use
Other font styles liked:
• Avenir Next

Requirements
Must have
• See project description
Should not have
• Nothing cheesy

```html
<!DOCTYPE html>
<html lang="en">
<head>
<meta charset="utf-8">
<title>Varnhill Lending – Business Card</title>
<link href="https://fonts.googleapis.com/css2?family=Nunito+Sans:wght@300;400&family=Open+Sans:wght@400;700&display=swap" rel="stylesheet">
<style>
  :root {
    --dark-gray: #2c3539;
    --light-gray: #576870;
    --white: #ffffff;
    --stage: #e6e7e8;
    --muted: #8a9aa1;
    --ring-dark: #7e9098;
    --text: #3a4448;
  }
  * { margin: 0; padding: 0; box-sizing: border-box; }
  html, body { width: 1200px; height: 1000px; overflow: hidden; }
  body { background: var(--stage); position: relative; font-family: "Open Sans", sans-serif; }

  .card {
    position: absolute;
    left: 267px;
    width: 665px;
    height: 397px;
    border-radius: 22px;
    overflow: hidden;
  }
  .card--back { top: 75px; background: var(--dark-gray); }
  .card--front { top: 533px; background: var(--white); }

  .emblem {
    position: absolute;
    border-radius: 50%;
    display: flex;
    align-items: center;
    justify-content: center;
    text-align: center;
    font-family: "Nunito Sans", sans-serif;
    font-weight: 300;
  }
  .card--back .emblem {
    left: 198px; top: 50px; width: 268px; height: 268px;
    border: 1.5px solid var(--ring-dark);
    color: var(--muted);
    font-size: 28px; line-height: 1.15;
  }
  .card--front .emblem {
    left: 58px; top: 78px; width: 242px; height: 242px;
    border: 1.5px solid var(--dark-gray);
    color: var(--light-gray);
    font-size: 26px; line-height: 1.15;
  }

  .services {
    position: absolute;
    left: 0; right: 0; top: 346px;
    text-align: center;
    font-family: "Nunito Sans", sans-serif;
    font-size: 17px;
    color: var(--muted);
  }

  .divider {
    position: absolute;
    left: 346px; top: 97px;
    width: 2px; height: 204px;
    background: var(--dark-gray);
  }

  .details {
    position: absolute;
    left: 393px; top: 88px;
    color: var(--light-gray);
    font-size: 16px;
    line-height: 24px;
  }
  .details__name {
    font-weight: 700;
    font-size: 20px;
    color: var(--dark-gray);
    letter-spacing: 0.3px;
    line-height: 26px;
  }
  .details__address { margin-top: 12px; }
  .details__contact { margin-top: 10px; list-style: none; }
  .details__contact li { display: flex; align-items: center; height: 23.5px; }
  .details__contact svg { width: 15px; height: 15px; margin-right: 7px; fill: var(--dark-gray); flex: none; }
</style>
</head>
<body>

<section class="card card--back" aria-label="Card back">
  <div class="emblem">Varnhill<br>Lending</div>
  <p class="services">Mortgage Loans - Reverse Mortgages - Private Money Loans</p>
</section>

<section class="card card--front" aria-label="Card front">
  <div class="emblem">Varnhill<br>Lending</div>
  <div class="divider"></div>
  <div class="details">
    <p class="details__name">MARCO LINDQVIST</p>
    <p class="details__title">Chief Managing Officer</p>
    <p class="details__address">418 Maple Ridge Ave, #120<br>Fairview TX 75069</p>
    <ul class="details__contact">
      <li>
        <svg viewBox="0 0 16 16" aria-hidden="true"><path d="M1 6c0-3 3-4 7-4s7 1 7 4v1h-4V5.5H5V7H1z"/><path d="M3 8h10l1 6H2z"/></svg>
        + 000 000 0000
      </li>
      <li>
        <svg viewBox="0 0 16 16" aria-hidden="true"><rect x="4" y="1" width="8" height="4"/><rect x="1" y="6" width="14" height="6" rx="1"/><rect x="4" y="10" width="8" height="5" fill="#fff" stroke="#2c3539" stroke-width="1.5"/></svg>
        + 000 000 0000
      </li>
      <li>
        <svg viewBox="0 0 16 16" aria-hidden="true"><rect x="1" y="3" width="14" height="10"/><path d="M1.5 3.5 8 9l6.5-5.5" fill="none" stroke="#fff" stroke-width="1.3"/></svg>
        info@varnhill-lending.com
      </li>
      <li>
        <svg viewBox="0 0 16 16" aria-hidden="true"><circle cx="8" cy="8" r="7"/><path d="M1 8h14M8 1c-3 3-3 11 0 14M8 1c3 3 3 11 0 14" fill="none" stroke="#fff" stroke-width="1.1"/></svg>
        www.varnhill-lending.com
      </li>
    </ul>
  </div>
</section>

</body>
</html>
```